Healthcare Review Meeting

We are a manufacturing company that provides health insurance to our 230+ employees. We have been trying to educate them on understanding and utilizing their healthcare benefits. We would like to reach out to the spouses to provide them with the same information. We are a predominately male company and we want to reach the spouses, who likely make all the healthcare decisions. I attached a sample of what we are looking for, but it needs some sprucing up.

Industry/Entity Type

Health Insurance

```html
<!DOCTYPE html>
<html lang="en">
<head>
<meta charset="utf-8">
<title>Understanding Your Health Insurance – Postcard</title>
<link rel="stylesheet" href="https://fonts.googleapis.com/css2?family=Jost:wght@400;500&family=Oswald:wght@500;600&display=swap">
<style>
  :root {
    --backdrop: #2b2b2b;
    --card: #ffffff;
    --navy: #2b2f8f;
    --green: #5cb94a;
    --green-dark: #1e8a3c;
    --teal-light: #d8eff4;
    --teal: #7ecfdc;
    --ink: #3a3a3a;
    --rule: #555555;
  }
  * { box-sizing: border-box; margin: 0; padding: 0; }
  html, body { width: 900px; height: 1200px; overflow: hidden; }
  body { background: var(--backdrop); position: relative; font-family: "Jost", sans-serif; }

  .card { position: absolute; left: 98px; width: 705px; background: var(--card); overflow: hidden; }
  .card--front { top: 40px; height: 544px; }
  .card--back { top: 625px; height: 545px; }

  /* front */
  .hero-photo {
    position: absolute; left: 0; top: 0; width: 705px; height: 330px;
    background:
      radial-gradient(circle at 500px 160px, #9ccf4a 0, #8cc43e 90px, rgba(140,196,62,0) 140px),
      linear-gradient(100deg, #c9ced4 0%, #eef0f2 35%, #f4f4f4 60%, #e2e4e6 100%);
  }
  .hero-title {
    position: absolute; left: 52px; top: 62px;
    font-family: "Oswald", sans-serif; font-weight: 600; color: var(--navy);
    line-height: 1; text-shadow: 0 0 3px #fff, 0 0 3px #fff;
  }
  .hero-title__main { display: block; font-size: 78px; letter-spacing: 1px; }
  .hero-title__sub { display: block; font-size: 46px; margin-top: 8px; letter-spacing: 0.5px; }

  .front-band {
    position: absolute; left: 0; top: 310px; width: 705px; height: 234px;
    background: linear-gradient(180deg, #a9dfe8 0%, var(--teal-light) 100%);
  }
  .front-wings { position: absolute; left: 0; top: 290px; }

  .message-panel {
    position: absolute; left: 52px; top: 288px; width: 600px; height: 230px;
    background: var(--green); border-radius: 14px;
  }
  .message-panel__frame {
    position: absolute; left: 14px; top: 10px; right: 14px; bottom: 10px;
    border: 3px solid #fff; border-radius: 10px;
  }
  .message-panel__divider {
    position: absolute; left: 390px; top: 20px; width: 2px; height: 170px; background: rgba(255,255,255,0.7);
  }
  .headline {
    position: absolute; left: 53px; top: 40px; color: #fff; line-height: 1; font-weight: 400;
  }
  .headline__line1 { display: block; font-size: 34px; letter-spacing: 0.5px; }
  .headline__line2 { display: flex; align-items: flex-end; margin-top: 8px; }
  .headline__your { font-size: 28px; border-bottom: 3px solid #fff; padding-bottom: 2px; margin-right: 4px; }
  .headline__health { font-size: 50px; }
  .headline__line3 { display: block; font-size: 54px; margin-top: 6px; }
  .invite {
    position: absolute; left: 400px; top: 30px; width: 170px;
    color: #fff; text-align: center; font-size: 26px; line-height: 33px;
  }

  /* back */
  .details-panel {
    position: absolute; left: 24px; top: 25px; width: 361px; height: 495px;
    background: linear-gradient(160deg, #cfeaf3 0%, #e6f4f8 50%, #d2ecf3 100%);
  }
  .company { position: absolute; left: 44px; top: 40px; color: var(--navy); font-size: 24px; line-height: 30px; }
  .address { position: absolute; left: 44px; top: 76px; color: var(--ink); font-size: 22px; line-height: 30px; }

  .event-box {
    position: absolute; left: 0; top: 151px; width: 347px; height: 214px; background: var(--green);
  }
  .event-box__frame {
    position: absolute; left: 20px; top: 14px; width: 313px; height: 186px; border: 3px solid #fff;
  }
  .event-box__text {
    position: absolute; left: 45px; top: 30px; color: #fff; text-transform: uppercase;
    font-size: 24px; line-height: 30px;
  }
  .event-box__when { margin-top: 6px; text-transform: none; font-size: 23px; line-height: 30px; font-weight: 500; }
  .event-box__when .date { text-transform: uppercase; }

  .rsvp { position: absolute; left: 44px; top: 380px; font-size: 22px; line-height: 31px; color: var(--ink); }
  .rsvp__label { color: var(--navy); }

  .brand {
    position: absolute; left: 46px; top: 466px; display: flex; align-items: center; gap: 8px;
    color: var(--navy); font-size: 22px; font-weight: 500; text-transform: uppercase; letter-spacing: 0.5px;
  }
  .brand__mark { width: 22px; height: 22px; background: var(--navy); }

  .stamp-box { position: absolute; left: 587px; top: 37px; width: 82px; height: 92px; border: 1px solid var(--rule); }
  .address-line { position: absolute; left: 429px; width: 240px; height: 1px; background: var(--rule); }
</style>
</head>
<body>

<section class="card card--front">
  <div class="hero-photo" role="img" aria-label="Doctor holding a green apple with a red question mark beside it"></div>
  <h1 class="hero-title">
    <span class="hero-title__main">HEALTH</span>
    <span class="hero-title__sub">INSURANCE</span>
  </h1>

  <div class="front-band"></div>
  <svg class="front-wings" width="705" height="100" viewBox="0 0 705 100" aria-hidden="true">
    <polygon points="22,52 60,38 60,70" fill="var(--green-dark)"/>
    <polygon points="0,70 60,50 60,90 0,95" fill="var(--navy)"/>
    <polygon points="683,52 645,38 645,70" fill="var(--green-dark)"/>
    <polygon points="705,70 645,50 645,90 705,95" fill="var(--navy)"/>
  </svg>

  <div class="message-panel">
    <div class="message-panel__frame"></div>
    <div class="message-panel__divider"></div>
    <h2 class="headline">
      <span class="headline__line1">UNDERSTANDING</span>
      <span class="headline__line2"><span class="headline__your">YOUR</span><span class="headline__health">HEALTH</span></span>
      <span class="headline__line3">INSURANCE</span>
    </h2>
    <p class="invite">Come<br>Join Us<br>And<br>We Will<br>Explain It!</p>
  </div>
</section>

<section class="card card--back">
  <div class="details-panel"></div>

  <p class="company">Keystone Metalworks Inc</p>
  <p class="address">18 Foundry Lane Millbrook,<br>NJ 08800</p>

  <div class="event-box">
    <div class="event-box__frame"></div>
    <div class="event-box__text">
      <p>Join us for our<br>exciting events:</p>
      <p class="event-box__when"><span class="date">April 2, 2016</span><br>10:00am to 12:00pm<br>or 2:00pm to 4:00pm</p>
    </div>
  </div>

  <p class="rsvp"><span class="rsvp__label">RSVP: Carol Whitfield</span><br>(555) 014-2200 Ext 1042</p>
  <p class="brand"><span class="brand__mark"></span>Keystone Metalworks</p>

  <div class="stamp-box"></div>
  <div class="address-line" style="top:311px"></div>
  <div class="address-line" style="top:348px"></div>
  <div class="address-line" style="top:386px"></div>
</section>

</body>
</html>
```